Therapy Dog Business need a brochure

I need a brochure designed for my Canine Assisted Therapy business in Victoria Australia. I have a logo already and info and photos to upload.
Best as white background and using the colours from the logo please
Updates

Hi Everyone,
I am sorry to have to revise the brief. I have added three new photos I was unable to add due to the size. I have had to wait for my photographer to change the size to add them today. I have been really inspired by all the work you have done so far. Thank you.
Could you please add the following on the brochure. (Under the individual dogs photo)
1. Juniper is the white dog. Please add the following under her picture. Juniper is one of the first Court Dogs in Australia. Working in Victoria, she has worked in the following Courts. The Ostrander Inquest Bench, The Dunmore Justice Hall in Collingwood, and the Brackwell Tribunal in Melbourne CBD. Her ability to use her intuition for clients is inspiring. Please contact us for potential use in Courts. Juniper has worked at the Harrowgate Safety College, and at STAVE at Har Saf. She is a stunning dog!
2. Barnaby is the golden dog. Barnaby is Junipers son, and had her instinct of intuition of who needs his help. Barnaby has an incredible soft approach as does his mother Juniper. He is incredibly safe with young children, and yet has a playful nature for adolescents and adults alike. He is soft and caring, and like his mother will go to those who need him most. Barnaby like his mother has worked at Harrowgate Safety, his time at HS included the Harrowgate Safety Council (HSC) Both he and his mother have very impressive CV'S!
3. Pepper the black dog. Pepper is my Therapy and Assistance dog "trainer" she is safe and stable with all the dogs and people I train for Therapy Dog Training and Assistance Dog Training. She has also been with me on my journey as a Counsellor and I have been able to work alongside her and Juniper for Counselling sessions.
She is soft, caring, and also intuitive. I am incredibly grateful for her help, as well as Juniper and Barnaby.
ALSO I am so sorry to add this but could you also add the following: Maybe in dot point?
Court Dog Availability
Therapy Dog Visits - Lawyers - Courts - Child Protection
Police Station / Ambulance Station / Fire Station - Visits
Private Therapy Dog Sessions
website and email confirmation coming soon. Thank you

3. Pepper the black dog.

Target Market(s)

First Responders

Requirements
Must have
• All the photos provided.
Should not have
• Generic photos

```html
<!DOCTYPE html>
<html lang="en">
<head>
<meta charset="utf-8">
<title>Canine-Assisted Therapy Brochure</title>
<link rel="stylesheet" href="https://fonts.googleapis.com/css2?family=Anton&family=Montserrat:wght@400;500;600&family=Poppins:ital,wght@0,500;0,600;0,700;1,600;1,700;1,800&family=Yellowtail&display=swap">
<style>
:root{
  --stage:#2e2e2e;
  --paper:#ffffff;
  --ink:#5a5a5a;
  --ink-dark:#333333;
  --orange:#ef9a4f;
  --orange-soft:#f3a46a;
  --coral:#e07a78;
  --pink:#e78d8c;
  --burgundy:#6e2a3c;
  --burgundy-deep:#5a1f31;
  --brick:#b4402f;
  --brick-dark:#8f2a22;
  --gold-top:#f0b24a;
  --gold-bottom:#cf6a3d;
  --grey-top:#ffffff;
  --grey-bottom:#cfcfcf;
  --night-top:#262626;
  --night-bottom:#7a7a7a;
  --sofa:#7f95d6;
  --cream:#fde9dc;
}
*{margin:0;padding:0;box-sizing:border-box}
html,body{width:1200px;height:800px;overflow:hidden;background:var(--stage)}
.page{position:absolute;top:25px;width:530px;height:750px;background:var(--paper);overflow:hidden;font-family:"Montserrat",sans-serif;color:var(--ink)}
.page--inside{left:50px}
.page--cover{left:620px}
.abs{position:absolute}

/* inside page */
.section-title{position:absolute;left:23px;font-family:"Poppins",sans-serif;font-weight:600;font-size:15px;color:var(--orange);background:linear-gradient(90deg,var(--orange),var(--coral));-webkit-background-clip:text;background-clip:text;-webkit-text-fill-color:transparent}
.rule{position:absolute;left:0;height:1px;background:#b8b8b8}
.intro{position:absolute;left:23px;top:45px;width:266px;font-size:8.8px;line-height:12.4px}
.hero-photo{position:absolute;left:296px;top:-81px;width:296px;height:296px;border-radius:50%;background:linear-gradient(180deg,#b9674d 0%,#c98768 45%,#8fa0da 62%,var(--sofa) 100%)}
.dot{position:absolute;border-radius:50%}
.benefit__icon{position:absolute;left:25px;width:24px;height:24px;border-radius:50%;background:linear-gradient(135deg,var(--pink),var(--coral));display:flex;align-items:center;justify-content:center}
.benefit__title{position:absolute;left:57px;font-family:"Poppins",sans-serif;font-weight:600;font-size:11.5px;line-height:13px;color:#444}
.benefit__text{position:absolute;left:26px;width:480px;font-size:8.8px;line-height:12.5px}
.why-title{position:absolute;left:25px;top:434px;font-family:"Poppins",sans-serif;font-weight:700;font-size:23px;background:linear-gradient(90deg,var(--orange),var(--coral));-webkit-background-clip:text;background-clip:text;-webkit-text-fill-color:transparent}
.why-band{position:absolute;left:0;top:0}
.reason{position:absolute;top:486px;width:150px;text-align:center;color:#fff}
.reason__icon{width:40px;height:40px;margin:0 auto;border-radius:50%;background:var(--orange-soft);display:flex;align-items:center;justify-content:center}
.reason__title{margin-top:9px;font-family:"Poppins",sans-serif;font-weight:600;font-size:11.5px;line-height:12.5px}
.reason__text{margin-top:7px;font-size:9px;line-height:11.8px;color:var(--cream)}
.cta{position:absolute;left:83px;top:648px;width:365px;height:69px;border-radius:35px;background:var(--orange-soft);color:#fff;text-align:center;padding-top:6px}
.cta__title{font-family:"Poppins",sans-serif;font-style:italic;font-weight:700;font-size:12.5px}
.cta__text{margin:2px auto 0;width:320px;font-size:7.6px;line-height:9.6px;font-weight:500}
.contact{position:absolute;display:flex;align-items:center;gap:5px;font-family:"Poppins",sans-serif;font-style:italic;font-weight:700}
.contact--inside{left:21px;top:723px;color:var(--burgundy)}
.contact__phone{font-size:17.5px}
.contact__web{position:absolute;left:177px;top:729px;font-family:"Poppins",sans-serif;font-style:italic;font-weight:600;font-size:11.5px;color:var(--burgundy)}

/* cover */
.brick-photo{position:absolute;left:0;top:0}
.cover-kicker{position:absolute;left:0;width:530px;top:13px;text-align:center;font-family:"Poppins",sans-serif;font-style:italic;font-weight:600;font-size:16px;color:#fff}
.cover-title{position:absolute;left:0;width:530px;top:30px;text-align:center;font-family:"Anton",sans-serif;font-size:60px;line-height:72px;color:#fff;letter-spacing:.5px}
.cover-script{position:absolute;left:0;width:530px;top:86px;text-align:center;font-family:"Yellowtail",cursive;font-size:76px;line-height:100px;color:#fff}
.dog-card{position:absolute;top:290px;width:150px;height:300px;border-radius:75px;text-align:center;padding:48px 7px 0}
.dog-card--golden{left:25px;background:linear-gradient(180deg,var(--gold-top),var(--gold-bottom));color:#fff;height:296px}
.dog-card--white{left:190px;background:linear-gradient(180deg,var(--grey-top),var(--grey-bottom));color:var(--ink-dark)}
.dog-card--black{left:355px;background:linear-gradient(180deg,var(--night-top),var(--night-bottom));color:#fff}
.dog-card__name{font-family:"Poppins",sans-serif;font-weight:600;font-size:11.5px;line-height:12.5px}
.dog-card__text{margin-top:4px;font-size:7.6px;line-height:10.5px}
.dog-portrait{position:absolute;top:180px;width:160px;height:160px;border-radius:50%;border:6px solid #fff;background:linear-gradient(180deg,#b24a35 0%,#b24a35 38%,#8da0dc 55%,var(--sofa) 100%)}
.dog-portrait--golden{left:20px}
.dog-portrait--white{left:185px}
.dog-portrait--black{left:350px}
.cover-footer{position:absolute;left:0;top:0}
.brand-mark{position:absolute;left:36px;top:605px;width:130px;height:130px;border-radius:50%;background:#fff;display:flex;align-items:center;justify-content:center;font-family:"Poppins",sans-serif;font-weight:700;font-size:16px;color:var(--burgundy);text-align:center;line-height:18px}
.availability{position:absolute;left:195px;top:632px;height:22px;padding:0 8px;border-radius:11px;background:var(--orange);color:#fff;font-family:"Poppins",sans-serif;font-weight:600;font-size:13px;line-height:22px}
.service{position:absolute;left:198px;font-family:"Poppins",sans-serif;font-size:10.8px;color:#fff;white-space:nowrap}
.service b{font-weight:600}
.service-rule{position:absolute;left:194px;width:336px;height:1px;background:rgba(255,255,255,.6)}
.contact--cover{left:196px;top:718px;color:#fff}
.contact--cover .contact__phone{font-size:20px}
.cover-web{position:absolute;left:372px;top:721px;font-family:"Poppins",sans-serif;font-style:italic;font-weight:700;font-size:10px;line-height:12px;color:#fff}
</style>
</head>
<body>

<!-- Inside page -->
<section class="page page--inside">
  <div class="hero-photo" role="img" aria-label="Photo of two golden dogs and a black dog resting on a blue sofa in front of a brick wall"></div>
  <span class="dot" style="left:294px;top:125px;width:24px;height:24px;background:var(--coral)"></span>
  <span class="dot" style="left:470px;top:161px;width:66px;height:66px;background:linear-gradient(135deg,var(--orange),#f0b24a)"></span>

  <h2 class="section-title" style="top:12px">What is Canine Assisted Therapy?</h2>
  <div class="rule" style="top:34px;width:288px"></div>
  <p class="intro">Canine Assisted Therapy (CAT) is a unique form of therapy that integrates trained therapy dogs into the healing process. By working alongside licensed therapists, these compassionate and well-trained dogs help support individuals in overcoming emotional, physical, and psychological challenges. This innovative approach promotes healing, reduces stress, and enhances overall well-being.</p>

  <h2 class="section-title" style="top:161px">Benefits of Canine Assisted Therapy</h2>
  <div class="rule" style="top:187px;width:321px"></div>

  <span class="benefit__icon" style="top:196px"><svg width="13" height="13" viewBox="0 0 24 24"><path fill="#fff" d="M12 21s-8-5.2-8-11a4.5 4.5 0 0 1 8-2.8A4.5 4.5 0 0 1 20 10c0 5.8-8 11-8 11z"/></svg></span>
  <h3 class="benefit__title" style="top:198px">Emotional Support<br>and Comfort</h3>
  <p class="benefit__text" style="top:221px">Therapy dogs provide immediate emotional support, offering comfort and companionship during therapy sessions. Their calming presence helps reduce feelings of anxiety, stress, and depression, and grief, creating a safe and nurturing environment for healing.</p>

  <span class="benefit__icon" style="top:274px"><svg width="14" height="14" viewBox="0 0 24 24" fill="#fff"><circle cx="7" cy="8" r="2.3"/><circle cx="12" cy="6" r="2.3"/><circle cx="17" cy="8" r="2.3"/><ellipse cx="12" cy="15" rx="4.5" ry="3.8"/></svg></span>
  <h3 class="benefit__title" style="top:279px">Stress Relief and<br>Relaxation</h3>
  <p class="benefit__text" style="top:302px;width:500px">Interacting with dogs has been proven to reduce cortisol (stress hormone) levels and increase serotonin and oxytocin, the “feel-good” hormones. This natural relief from stress makes Canine Assisted Therapy an ideal option for individuals dealing with anxiety, trauma, PTSD, and grief.</p>

  <span class="benefit__icon" style="top:352px"><svg width="13" height="13" viewBox="0 0 24 24"><path fill="none" stroke="#fff" stroke-width="2.6" d="M5 12.5l4.5 4.5L19 7.5"/></svg></span>
  <h3 class="benefit__title" style="top:357px">Improved Mental<br>Health</h3>
  <p class="benefit__text" style="top:380px;width:500px">Therapy dogs encourage social interaction, communication, and emotional expression, helping individuals address mental health challenges such as depression, anxiety, PTSD, and grief. The unconditional love and companionship of a dog can foster trust and openness during therapy sessions.</p>

  <h2 class="why-title">Why Choose Canine Assisted Therapy?</h2>

  <svg class="why-band" width="530" height="750" viewBox="0 0 530 750" aria-hidden="true">
    <defs>
      <linearGradient id="bandFill" x1="0" y1="0" x2="0" y2="1">
        <stop offset="0" stop-color="#6e2a3c"/>
        <stop offset="1" stop-color="#8a3a44"/>
      </linearGradient>
    </defs>
    <path fill="url(#bandFill)" d="M0 480 q11 -9 22 0 t22 0 t22 0 t22 0 t22 0 t22 0 t22 0 t22 0 t22 0 t22 0 t22 0 t22 0 t22 0 t22 0 t22 0 t22 0 t22 0 t22 0 t22 0 t22 0 t22 0 t22 0 t22 0 t22 0 L530 480 V683 Q300 700 160 668 Q50 640 0 590 Z"/>
  </svg>

  <div class="reason" style="left:9px">
    <div class="reason__icon"><svg width="22" height="22" viewBox="0 0 24 24"><path fill="#fff" d="M12 21s-8-5.2-8-11a4.5 4.5 0 0 1 8-2.8A4.5 4.5 0 0 1 20 10c0 5.8-8 11-8 11z"/></svg></div>
    <h3 class="reason__title">Proven<br>Effectiveness</h3>
    <p class="reason__text">Studies and testimonials highlight the positive effects therapy dogs have on emotional, psychological and physical health.</p>
  </div>
  <div class="reason" style="left:190px">
    <div class="reason__icon"><svg width="22" height="22" viewBox="0 0 24 24" fill="#fff"><circle cx="7" cy="8" r="2.3"/><circle cx="12" cy="6" r="2.3"/><circle cx="17" cy="8" r="2.3"/><ellipse cx="12" cy="15" rx="4.5" ry="3.8"/></svg></div>
    <h3 class="reason__title">Non-Invasive<br>and Gentle</h3>
    <p class="reason__text">Therapy dogs provide a natural and non-threatening way to engage with patients, making it accessible for individuals who may feel apprehensive about traditional therapy methods.</p>
  </div>
  <div class="reason" style="left:364px">
    <div class="reason__icon"><svg width="22" height="22" viewBox="0 0 24 24"><path fill="#fff" d="M12 2l8 3v6c0 5-3.5 9-8 11-4.5-2-8-6-8-11V5z"/><path fill="none" stroke="#ef9a4f" stroke-width="2.4" d="M8 12l3 3 5-6"/></svg></div>
    <h3 class="reason__title">Safe and<br>Trustworthy</h3>
    <p class="reason__text">All therapy dogs are carefully trained to work with professionals, ensuring that interactions are safe, beneficial, and appropriate for all individuals.</p>
  </div>

  <div class="cta">
    <p class="cta__title">Join the Healing Journey Today!</p>
    <p class="cta__text">Whether you are seeking emotional support or mental health improvement, Canine Assisted Therapy offers a unique and compassionate approach to healing. Connect with us today to learn more about how a therapy dog can help enhance your life and well-being.</p>
  </div>

  <div class="contact contact--inside">
    <svg width="15" height="15" viewBox="0 0 24 24"><circle cx="12" cy="12" r="10.5" fill="none" stroke="currentColor" stroke-width="1.8"/><path fill="currentColor" d="M8.3 6.5h2l1 2.8-1.3 1.1a7 7 0 0 0 3.6 3.6l1.1-1.3 2.8 1v2c0 .6-.5 1-1 1A9.3 9.3 0 0 1 7.3 7.5c0-.6.4-1 1-1z"/></svg>
    <span class="contact__phone">0400 123 987</span>
  </div>
  <p class="contact__web">www.kindredpaws.example | info@kindredpaws.example</p>
</section>

<!-- Cover page -->
<section class="page page--cover">
  <svg class="brick-photo" width="530" height="360" viewBox="0 0 530 360" role="img" aria-label="Photo of a red brick wall behind the heading">
    <defs>
      <linearGradient id="brickFill" x1="0" y1="0" x2="1" y2="1">
        <stop offset="0" stop-color="#b8372c"/>
        <stop offset=".5" stop-color="#c2503a"/>
        <stop offset="1" stop-color="#a8382c"/>
      </linearGradient>
    </defs>
    <path fill="url(#brickFill)" d="M0 0H530V228Q505 330 440 352H90Q25 330 0 250Z"/>
  </svg>

  <p class="cover-kicker">Discover the Healing Power of</p>
  <h1 class="cover-title">Canine-Assisted</h1>
  <p class="cover-script">Therapy</p>

  <article class="dog-card dog-card--golden">
    <h2 class="dog-card__name">Barnaby is<br>the Golden Dog</h2>
    <p class="dog-card__text">Barnaby is Junipers son, and had her instinct of intuition of who needs his help. Barnaby has an incredible soft approach as does his mother Juniper. He is incredibly safe with young children, and yet has a playful nature for adolescents and adults alike. He is soft and caring, and like his mother will go to those who need him most. Barnaby like his mother has worked at Harrowgate Safety, his time at HS included the Harrowgate Safety Council (HSC) Both he and his mother have very impressive CV'S!</p>
  </article>
  <article class="dog-card dog-card--white">
    <h2 class="dog-card__name">Juniper is<br>the White Dog</h2>
    <p class="dog-card__text">Please add the following under her picture. Juniper is one of the first Court Dogs in Australia. Working in Victoria, she has worked in the following Courts. The Ostrander Inquest Bench, The Dunmore Justice Hall in Collingwood, and the Brackwell Tribunal in Melbourne CBD. Her ability to use her intuition for clients is inspiring. Please contact us for potential use in Courts. Juniper has worked at the Harrowgate Safety College, and at STAVE at Har Saf. She is a stunning dog!</p>
  </article>
  <article class="dog-card dog-card--black">
    <h2 class="dog-card__name">Pepper<br>the Black Dog</h2>
    <p class="dog-card__text">Pepper is my Therapy and Assistance dog "trainer" she is safe and stable with all the dogs and people I train for Therapy Dog Training and Assistance Dog Training. She has also been with me on my journey as a Counsellor and I have been able to work alongside her and Juniper for Counselling sessions. She is soft, caring, and also intuitive. I am incredibly grateful for her help, as well as Juniper and Barnaby.</p>
  </article>

  <div class="dog-portrait dog-portrait--golden" role="img" aria-label="Photo of Barnaby, the golden dog, lying on a blue sofa"></div>
  <div class="dog-portrait dog-portrait--white" role="img" aria-label="Photo of Juniper, the white dog, lying on a blue sofa"></div>
  <div class="dog-portrait dog-portrait--black" role="img" aria-label="Photo of Pepper, the black dog, lying on a blue sofa"></div>

  <span class="dot" style="left:503px;top:307px;width:18px;height:18px;background:var(--orange)"></span>
  <span class="dot" style="left:15px;top:578px;width:18px;height:18px;background:var(--coral)"></span>

  <svg class="cover-footer" width="530" height="750" viewBox="0 0 530 750" aria-hidden="true">
    <defs>
      <linearGradient id="footerFill" x1="0" y1="0" x2="1" y2="0">
        <stop offset="0" stop-color="#e89293"/>
        <stop offset=".45" stop-color="#d06e5c"/>
        <stop offset="1" stop-color="#a9442e"/>
      </linearGradient>
    </defs>
    <path fill="url(#footerFill)" d="M0 648Q140 616 320 613Q470 610 530 572V750H0Z"/>
  </svg>

  <div class="brand-mark">Kindred<br>Paws</div>

  <p class="availability">Court Dog Availability</p>
  <p class="service" style="top:657px"><b>Therapy Dog Visits:</b> Lawyers - Courts - Child Protection</p>
  <div class="service-rule" style="top:674px"></div>
  <p class="service" style="top:677px"><b>• Police Station&nbsp; • Ambulance Station&nbsp; • Fire Station</b></p>
  <div class="service-rule" style="top:694px"></div>
  <p class="service" style="top:697px"><b>Visits -</b> Private Therapy Dog Sessions</p>

  <div class="contact contact--cover">
    <svg width="17" height="17" viewBox="0 0 24 24"><circle cx="12" cy="12" r="10.5" fill="none" stroke="currentColor" stroke-width="1.8"/><path fill="currentColor" d="M8.3 6.5h2l1 2.8-1.3 1.1a7 7 0 0 0 3.6 3.6l1.1-1.3 2.8 1v2c0 .6-.5 1-1 1A9.3 9.3 0 0 1 7.3 7.5c0-.6.4-1 1-1z"/></svg>
    <span class="contact__phone">0400 123 987</span>
  </div>
  <p class="cover-web">www.kindredpaws.example<br>info@kindredpaws.example</p>
</section>

</body>
</html>
```